50 bday

It's my 50th bday and I need the invitation that we will be send by digital (mail and whatapp). One important aspect is that my bday is on day 2 month 2 of year 22 so this is going to be important things that I want to use it as the main theme as you can see in the attached example

```html
<!DOCTYPE html>
<html lang="es">
<head>
<meta charset="utf-8">
<title>50 Birthday – 2-2-22</title>
<link href="https://fonts.googleapis.com/css2?family=Abril+Fatface&family=Cinzel:wght@400&family=Libre+Baskerville:wght@700&family=Playfair+Display:wght@700&display=swap" rel="stylesheet">
<style>
  :root {
    --page: #ffffff;
    --gold-dark: #c4843f;
    --gold-mid: #dba863;
    --gold-light: #f3d9a0;
    --navy-deep: #041a3e;
    --navy-mid: #0a3d8f;
    --royal: #0a4aad;
    --ink: #111111;
    --white: #ffffff;
    --shadow: rgba(0, 0, 0, 0.35);
  }
  * { margin: 0; padding: 0; box-sizing: border-box; }
  html, body {
    width: 1200px;
    height: 1000px;
    overflow: hidden;
    background: var(--page);
  }
  .invitation {
    position: absolute;
    left: 74px;
    top: 130px;
    width: 1052px;
    height: 742px;
    background: linear-gradient(90deg, var(--gold-dark), var(--gold-light) 30%, var(--gold-mid) 60%, var(--gold-dark) 85%, var(--gold-light));
    box-shadow: 6px 10px 14px var(--shadow);
  }
  .invitation__field {
    position: absolute;
    left: 18px;
    top: 20px;
    right: 18px;
    bottom: 17px;
    background: linear-gradient(180deg, var(--navy-deep) 0%, var(--navy-mid) 30%, var(--royal) 45%, var(--navy-mid) 65%, var(--navy-deep) 100%);
  }
  .invitation__rule {
    position: absolute;
    left: 41px;
    top: 42px;
    width: 971px;
    height: 661px;
    border: 2px solid var(--gold-mid);
  }
  .corner-art {
    position: absolute;
    background: var(--gold-mid);
    border-radius: 6px;
  }
  .corner-art--top { left: 954px; top: 14px; width: 88px; height: 86px; }
  .corner-art--bottom { left: 26px; top: 634px; width: 92px; height: 82px; }
  .title {
    position: absolute;
    left: 0;
    width: 1200px;
    top: 226px;
    text-align: center;
    font-family: "Playfair Display", serif;
    font-weight: 700;
    font-size: 88px;
    line-height: 1;
    color: var(--white);
    text-shadow: 4px 3px 0 var(--ink);
    letter-spacing: 1px;
  }
  .date-tile {
    position: absolute;
    top: 385px;
    height: 150px;
    border-radius: 16px;
    background: linear-gradient(180deg, var(--gold-dark) 0%, var(--gold-light) 50%, var(--gold-dark) 100%);
    display: flex;
    align-items: center;
    justify-content: center;
    font-family: "Abril Fatface", "Playfair Display", serif;
    font-size: 150px;
    line-height: 1;
    color: var(--white);
    text-shadow: 5px 4px 0 var(--ink);
  }
  .date-tile--day { left: 189px; width: 172px; }
  .date-tile--month { left: 459px; width: 172px; }
  .date-tile--year { left: 729px; width: 256px; }
  .date-dash {
    position: absolute;
    top: 458px;
    width: 50px;
    height: 5px;
    background: var(--white);
  }
  .date-dash--first { left: 385px; }
  .date-dash--second { left: 655px; }
  .date-label {
    position: absolute;
    top: 552px;
    text-align: center;
    font-family: "Libre Baskerville", serif;
    font-weight: 700;
    font-size: 27px;
    line-height: 36px;
    color: var(--white);
    white-space: nowrap;
  }
  .date-label--day { left: 175px; width: 200px; }
  .date-label--month { left: 420px; width: 250px; }
  .date-label--year { left: 680px; width: 355px; }
  .details {
    position: absolute;
    left: 0;
    width: 1200px;
    top: 648px;
    text-align: center;
    font-family: "Cinzel", serif;
    font-weight: 400;
    font-size: 36px;
    line-height: 44px;
    letter-spacing: 1.5px;
    color: var(--white);
  }
</style>
</head>
<body>
  <main class="invitation">
    <div class="invitation__field"></div>
    <div class="invitation__rule"></div>
    <div class="corner-art corner-art--top" role="img" aria-label="Globo dorado decorativo"></div>
    <div class="corner-art corner-art--bottom" role="img" aria-label="Globo dorado decorativo"></div>
  </main>

  <h1 class="title">50 BIRTHDAY</h1>

  <div class="date-tile date-tile--day">2</div>
  <div class="date-dash date-dash--first"></div>
  <div class="date-tile date-tile--month">2</div>
  <div class="date-dash date-dash--second"></div>
  <div class="date-tile date-tile--year">22</div>

  <p class="date-label date-label--day">(dos)</p>
  <p class="date-label date-label--month">(febrero)</p>
  <p class="date-label date-label--year">(dos mil veintidós)</p>

  <p class="details">
    TE ESPERO A PARTIR DE LAS 7 P.M. EN LA<br>
    CASA DE LOS FAROLES EN EL BARRIO ANTIGUO<br>
    RSVP 8095550142
  </p>
</body>
</html>
```